"Tidelark Ministry" needs a logo design that represents a Christian family boating ministry

Mission Statement:
“Providing compassion, care and opportunities to create memories for marginalized groups of society through ocean therapy.”
Bible verse:
Colossians 3:12 – “Therefore, as God’s chosen people, holy and dearly loved, clothe yourselves with compassion, kindness, humility, gentleness and patience.”
Target Market(s)
HOMELESS (who have gone through shelters and are on the road to recovery)
CHURCH GROUPS
INJURED MILITARY VETERANS
YOUTH AT RISK (orphans, human trafficking survivors)
SICKLY (hospitalized who can get out once in a while)
CAREGIVERS (single moms, military spouses caring for injured vets, families of those in prison)
ELDERLY (retirement centers)
SMALL BUSINESS STAFF OUTINGS
SPECIAL EVENTS
Industry/Entity Type
Ministry
Contact Information for Business Card
Captain Glen Marbury @ 555-014-2931
Priscilla Marbury @ 555-018-6457
info@tidelarkministry-example.com
www.tidelarkministry-example.com (not active yet but hopefully, soon)
Requirements
Must have
- Catch-phrase words maybe for back of business card:
- "Tidelark --- Kindness --- Sharing days on the waves"
Nice to have
- Added 2 photo files just for visuals:
- 1 photo is of our boat.
- Other photo is our daughter's artwork on a cooler she made (for father's day gift)...might be nice and fun to incorporate daughter's artwork/inspiration into logo...but not sure if it looks to busy

```html
<!DOCTYPE html>
<html lang="en">
<head>
<meta charset="utf-8">
<title>Tidelark Ministry – Business Card</title>
<link href="https://fonts.googleapis.com/css2?family=Work+Sans:wght@400;500&display=swap" rel="stylesheet">
<style>
  :root{
    --page:#2a2a2c;
    --card-grey:#747579;
    --card-grey-dark:#5f6064;
    --white:#ffffff;
    --ink-light:#f2f2f3;
    --accent-blue:#3e4a8e;
    --logo-grey:#6c6d70;
  }
  *{box-sizing:border-box;margin:0;padding:0}
  html,body{width:1200px;height:900px;overflow:hidden}
  body{
    background:var(--page);
    font-family:"Work Sans",Arial,sans-serif;
    position:relative;
  }
  .card{
    position:absolute;
    left:280px;
    width:640px;height:366px;
    border-radius:22px;
    overflow:hidden;
    box-shadow:0 14px 30px rgba(0,0,0,.45);
    background:linear-gradient(135deg,var(--card-grey) 0%,var(--card-grey-dark) 100%);
  }
  .card--back{top:54px}
  .card--front{top:480px}
  .brand{
    position:absolute;
    font-weight:400;
    line-height:1;
    white-space:nowrap;
  }
  .card--back .brand{
    left:170px;top:130px;
    font-size:50px;color:var(--white);
  }
  .tagline{
    position:absolute;
    right:36px;bottom:34px;
    font-size:15px;color:var(--ink-light);
    letter-spacing:.2px;
  }
  .tagline .dot{margin:0 10px}
  .front-shape{position:absolute;inset:0}
  .card--front .brand{
    left:34px;top:78px;
    font-size:34px;color:var(--logo-grey);
  }
  .contact{
    position:absolute;
    right:32px;top:66px;
    text-align:right;
    color:var(--ink-light);
    white-space:nowrap;
  }
  .contact__name{font-size:19px;font-weight:500;letter-spacing:.5px}
  .contact__role{font-size:12px;letter-spacing:1px;margin-top:3px}
  .contact__address{font-size:12.5px;line-height:1.5;margin-top:20px}
  .contact__lines{margin-top:8px;font-size:12.5px;line-height:1.6}
  .contact__line{display:flex;justify-content:flex-end;align-items:center;gap:9px}
  .contact__line svg{width:11px;height:11px;flex:none}
</style>
</head>
<body>

<section class="card card--back" aria-label="Card back">
  <div class="brand">Tidelark Ministry</div>
  <p class="tagline">Tidelark<span class="dot">•</span>Kindness<span class="dot">•</span>Sharing days on the waves</p>
</section>

<section class="card card--front" aria-label="Card front">
  <svg class="front-shape" viewBox="0 0 640 366" preserveAspectRatio="none">
    <path d="M0,0 H350 C410,110 330,290 30,366 H0 Z" fill="#ffffff"/>
    <path d="M350,0 C410,110 330,290 30,366" fill="none" stroke="#3e4a8e" stroke-width="5"/>
  </svg>
  <div class="brand">Tidelark Ministry</div>
  <div class="contact">
    <div class="contact__name">GORDON HALVERSEN</div>
    <div class="contact__role">DIRECTOR</div>
    <div class="contact__address">2290 Lantern Cove Rd,<br>Ashgrove County, AB, T0X 1A2</div>
    <div class="contact__lines">
      <div class="contact__line">(555) 017-3364
        <svg viewBox="0 0 12 12"><path d="M3 1l2 2.5-1.2 1.3a7 7 0 0 0 3.4 3.4L8.5 7 11 9l-1.2 1.8C5 10.5 1.5 7 1.2 2.2Z" fill="#f2f2f3"/></svg>
      </div>
      <div class="contact__line">info@tidelarkministry-example.com
        <svg viewBox="0 0 12 12"><rect x="1" y="2.5" width="10" height="7" rx="1" fill="#f2f2f3"/><path d="M1.5 3l4.5 3.5L10.5 3" fill="none" stroke="#6a6b6f" stroke-width="1"/></svg>
      </div>
      <div class="contact__line">www.tidelarkministry-example.com
        <svg viewBox="0 0 12 12"><circle cx="6" cy="6" r="5" fill="#f2f2f3"/><path d="M1 6h10M6 1c2.5 2.5 2.5 7.5 0 10M6 1c-2.5 2.5-2.5 7.5 0 10" fill="none" stroke="#6a6b6f" stroke-width=".8"/></svg>
      </div>
    </div>
  </div>
</section>

</body>
</html>
```